Redesign Colorful Business Card

Please redesign the card attached. It is too busy. Please don't eliminate any of the words. The repetivite word "free" can be used less often.

Target Market(s)

College Students.

Contact Information for Business Card

The details listed in the attached image

Font styles to use
Sans Serif

Requirements
Must have
• A clear and simple presentation and must be attractive.

```html
<!DOCTYPE html>
<html lang="en">
<head>
<meta charset="utf-8">
<title>StudyNimbl Business Card</title>
<link rel="stylesheet" href="https://fonts.googleapis.com/css2?family=Open+Sans:wght@400;700;800&display=swap">
<style>
  :root {
    --bg: #e4e4e4;
    --green: #05d414;
    --blue: #1523c4;
    --white: #ffffff;
  }
  html, body {
    margin: 0;
    padding: 0;
    width: 1200px;
    height: 1200px;
    overflow: hidden;
    background: var(--bg);
    font-family: "Open Sans", Arial, sans-serif;
  }
  .canvas {
    position: relative;
    width: 1200px;
    height: 1200px;
    display: flex;
    align-items: center;
    justify-content: center;
  }
  .card {
    position: relative;
    width: 1050px;
    height: 640px;
    background: var(--green);
    overflow: hidden;
    box-shadow: 0 18px 40px rgba(0,0,0,0.18);
  }
  .card-shapes {
    position: absolute;
    inset: 0;
  }
  .brand {
    position: absolute;
    left: 0;
    right: 0;
    top: 170px;
    display: flex;
    align-items: center;
    justify-content: center;
    gap: 14px;
    color: var(--white);
    font-size: 40px;
    font-weight: 400;
    letter-spacing: 0.5px;
  }
  .brand-dot {
    width: 26px;
    height: 26px;
    border-radius: 50%;
    background: var(--white);
  }
  .taglines {
    position: absolute;
    left: 0;
    right: 0;
    top: 270px;
    margin: 0;
    padding: 0;
    list-style: none;
    text-align: center;
    color: var(--green);
    font-weight: 800;
    font-size: 33px;
    line-height: 50px;
    text-transform: uppercase;
  }
  .badge {
    position: absolute;
    width: 86px;
    height: 86px;
  }
  .badge-left { left: 112px; top: 252px; }
  .badge-right { left: 850px; top: 196px; }
  .badge text {
    font-family: "Open Sans", Arial, sans-serif;
    font-weight: 800;
    font-size: 17px;
    fill: var(--white);
  }
  .copyright {
    position: absolute;
    left: 0;
    right: 0;
    bottom: 0;
    height: 80px;
    display: flex;
    align-items: center;
    justify-content: center;
    color: var(--white);
    font-size: 19px;
    font-weight: 400;
  }
</style>
</head>
<body>
<main class="canvas">
  <section class="card">
    <svg class="card-shapes" viewBox="0 0 1050 640" width="1050" height="640" aria-hidden="true">
      <polygon points="525,0 1050,160 1050,560 0,560 0,155" fill="var(--blue)"/>
    </svg>

    <div class="brand">
      <span class="brand-dot"></span>
      <span class="brand-name">StudyNimbl.com</span>
    </div>

    <svg class="badge badge-left" viewBox="0 0 100 100" aria-hidden="true">
      <polygon fill="var(--green)" points="50,4 57,18 71,9 73,25 89,22 83,37 97,44 84,54 93,68 77,71 79,87 63,82 57,97 47,84 35,96 31,80 15,83 19,67 4,60 17,50 6,37 22,33 20,17 36,20 40,5"/>
      <text x="50" y="56" text-anchor="middle">FREE</text>
    </svg>
    <svg class="badge badge-right" viewBox="0 0 100 100" aria-hidden="true">
      <polygon fill="var(--green)" points="50,4 57,18 71,9 73,25 89,22 83,37 97,44 84,54 93,68 77,71 79,87 63,82 57,97 47,84 35,96 31,80 15,83 19,67 4,60 17,50 6,37 22,33 20,17 36,20 40,5"/>
      <text x="50" y="56" text-anchor="middle">FREE</text>
    </svg>

    <ul class="taglines">
      <li>Cut study time by up 50%</li>
      <li>Learn a subject without having to go to class</li>
      <li>Memirize anything quickly</li>
    </ul>

    <footer class="copyright">Copyright Nimbl Services, LLC 2013-2022 All Rights Reserved</footer>
  </section>
</main>
</body>
</html>
```